Business Card: RW Office Partners - Your tidy answer finder

Business Name: RW Office Partners
Website: www.rwofficepartners.com.au
Email: marisol@rwofficepartners.com.au
Mobile: 61 487 902 346
Facebook: @rwofficepartners
Instrgram: @rwofficepartners

Brading Colours:
HEX
#986474
#ddccd3
#7a8498
#c9d8e4
#000000
#ffffff

Tag Line: Your tidy answer finder

Link to DRAFT website:
https://helpdeskhub.sitebuilderx.com/rw-office-partners

About Page from the website:
My name is Marisol Bramwell, and I would love to assist you to become more productive in your day to day and achieve your business and personal goals.
My mission is to give you time, time to work on the important tasks of your business or to be able to spend more time with your family. I will take on the tasks you don’t have time for, don’t know well or simply don’t like to do.
I have an extensive background in Administration, Tender Coordination, Document Control, WHS and Quality Management working primarily in the Construction, Mining and Corporate World.
I am passionate about being organised, having order and making things in your life (and mine) easier! I love to watch something unfold and grow into something amazing! I am known for being the go-to problem solver, the organiser of all things, producing high standards of work even under pressure. I’m also a confident communicator, and I understand that you’re busy running your business.

Target Market(s)

Small to Medium Business who require assistance in their business by a virtual assistant.

Industry/Entity Type

Virtual Assistant

Contact Information for Business Card

Mobile: 61 487 902 346

Font styles to use
Sans Serif

Colors
ffffff

Requirements
Must have
• Branding Colours as outlined.
Contact Details as outlined.
Logo as provided.
Proper contact details - mobile, facebook, instragm, website.
Simple, Elegant, very clean looking.
Should not have
• Note cute with pictures.
Not too girly as still want to market to construction companies.

```html
<!DOCTYPE html>
<html lang="en">
<head>
<meta charset="utf-8">
<title>RW Office Partners – Business Card</title>
<link rel="stylesheet" href="https://fonts.googleapis.com/css2?family=Questrial&family=Lexend:wght@400;500&family=Arimo:wght@400;700&display=swap">
<style>
  :root {
    --mauve: #986474;
    --mauve-soft: #ddccd3;
    --slate: #7a8498;
    --slate-soft: #c9d8e4;
    --ink: #1a1a1a;
    --paper: #ffffff;
    --backdrop: #d9d9db;
    --rule: #d6d6d6;
  }
  * { margin: 0; padding: 0; box-sizing: border-box; }
  html, body { width: 1200px; height: 802px; overflow: hidden; }
  body { background: var(--backdrop); position: relative; font-family: "Arimo", Arial, sans-serif; }

  .card {
    position: absolute;
    top: 240px;
    width: 540px;
    height: 323px;
    background: var(--paper);
    box-shadow: 3px 4px 8px rgba(0,0,0,0.35);
    overflow: hidden;
  }
  .card--front { left: 36px; }
  .card--back { left: 624px; }

  .brand-name {
    position: absolute;
    right: 32px;
    top: 60px;
    font-family: "Questrial", sans-serif;
    font-size: 31px;
    line-height: 31px;
    letter-spacing: 1px;
    text-align: right;
    color: var(--slate);
    text-transform: uppercase;
  }
  .tagline {
    position: absolute;
    right: 35px;
    top: 136px;
    font-family: "Lexend", sans-serif;
    font-weight: 500;
    font-size: 12.5px;
    letter-spacing: 0.1px;
    color: var(--ink);
    text-transform: uppercase;
  }

  .name-row {
    position: absolute;
    left: 28px;
    right: 35px;
    top: 170px;
    display: flex;
    align-items: center;
    gap: 12px;
  }
  .holder-name {
    font-family: "Lexend", sans-serif;
    font-weight: 500;
    font-size: 18px;
    letter-spacing: 0.2px;
    color: var(--mauve);
    text-transform: uppercase;
    white-space: nowrap;
  }
  .name-rule {
    flex: 1;
    height: 1px;
    background: var(--rule);
  }

  .contact-list { position: absolute; left: 27px; top: 225px; list-style: none; }
  .contact-list li {
    display: flex; align-items: center; gap: 6px;
    height: 24px; font-size: 15px; color: var(--ink);
  }
  .contact-list li.contact-web { color: var(--mauve); }
  .contact-list svg { width: 17px; height: 17px; flex: none; }

  .social {
    position: absolute; right: 30px; top: 272px;
    display: flex; align-items: center; gap: 6px;
    font-size: 15px; color: var(--ink);
  }
  .social-dot {
    width: 10px; height: 10px; border-radius: 50%;
    background: var(--slate);
  }

  .band { position: absolute; bottom: 0; left: 0; width: 540px; height: 20px; }

  .back-half { position: absolute; top: 0; height: 100%; }
  .back-half--mauve { left: 0; width: 270px; background: var(--mauve); }
  .back-half--slate { left: 270px; width: 270px; background: var(--slate); }
  .back-name {
    position: absolute; left: 0; right: 0; top: 50%;
    transform: translateY(-50%);
    text-align: center;
    font-family: "Questrial", sans-serif;
    font-size: 34px;
    letter-spacing: 2px;
    color: var(--paper);
    text-transform: uppercase;
  }
</style>
</head>
<body>

<section class="card card--front" aria-label="Card front">
  <div class="brand-name">RW Office<br>Partners</div>
  <div class="tagline">Your tidy answer finder</div>

  <div class="name-row">
    <div class="holder-name">Marisol Bramwell</div>
    <div class="name-rule"></div>
  </div>

  <ul class="contact-list">
    <li class="contact-phone">
      <svg viewBox="0 0 16 16" aria-hidden="true"><rect x="1" y="1" width="14" height="14" rx="2" fill="none" stroke="#986474" stroke-width="1.3"/><path d="M5 4c-1 1-1 3 1 5s4 2 5 1l-1.5-1.5-1 .7c-1-.5-2-1.5-2.5-2.5l.7-1L5 4z" fill="#986474"/></svg>
      61 487 902 346
    </li>
    <li class="contact-email">
      <svg viewBox="0 0 16 16" aria-hidden="true"><path d="M1 3h14v10H1z" fill="#986474"/><path d="M1 3l7 6 7-6" fill="none" stroke="#fff" stroke-width="1.2"/></svg>
      marisol@rwofficepartners.com.au
    </li>
    <li class="contact-web">
      <svg viewBox="0 0 16 16" aria-hidden="true"><g fill="none" stroke="#986474" stroke-width="1.1"><circle cx="8" cy="8" r="6.5"/><ellipse cx="8" cy="8" rx="3" ry="6.5"/><path d="M1.5 8h13M2.5 4.5h11M2.5 11.5h11"/></g></svg>
      www.rwofficepartners.com.au
    </li>
  </ul>

  <div class="social"><span class="social-dot" aria-hidden="true"></span>@rwofficepartners</div>

  <svg class="band" viewBox="0 0 540 20" preserveAspectRatio="none" aria-hidden="true">
    <polygon points="0,10 298,10 294,20 0,20" fill="var(--mauve)"/>
    <polygon points="306,0 540,0 540,20 300,20" fill="var(--slate)"/>
  </svg>
</section>

<section class="card card--back" aria-label="Card back">
  <div class="back-half back-half--mauve"></div>
  <div class="back-half back-half--slate"></div>
  <div class="back-name">RW Office Partners</div>
</section>

</body>
</html>
```